Travel Blogger Business Card for roamquill.net

I need a two-sided business card for a travel blogging website. The card should be both professional and fun at the same time. This is for the website www.roamquill.net

I don't necessarily think that the current logo on the website needs to be used on the business card but it can be. I am very flexible with ideas

Target Market(s)

Travel agencies that will be met at a conference.

Industry/Entity Type

Travel

Contact Information for Business Card

Company Name: Roam Quill.net
Name: Bertrand Olesky
Voice: +1-(345)-402-7731
Address: Coral Reach Shore, Grand Cayman, Cayman Islands
Email: ceo@roamquill.net

Colors
0592cd
0355a3
3176b5
33a6d7
85cae6
85acd3

Requirements
Must have
• Website address and name should be bigger than address, phone number, and email.

```html
<!DOCTYPE html>
<html lang="en">
<head>
<meta charset="utf-8">
<title>Roam Quill.net — Business Card</title>
<link rel="stylesheet" href="https://fonts.googleapis.com/css2?family=Source+Sans+3:ital,wght@0,400;0,600;0,700;1,400&display=swap">
<style>
  :root {
    --brand-blue: #1ba5cf;
    --ink-dark: #222426;
    --ink-text: #3c3c3c;
    --rule-grey: #b9b9b9;
    --card-white: #ffffff;
    --backdrop: #e4e4e4;
  }
  * { box-sizing: border-box; margin: 0; padding: 0; }
  html, body {
    width: 1200px; height: 987px; overflow: hidden;
    background: var(--backdrop);
    font-family: "Source Sans 3", "Myriad Pro", sans-serif;
  }
  .canvas { position: relative; width: 1200px; height: 987px; }
  .card {
    position: absolute; left: 293px; width: 615px; height: 352px;
    box-shadow: 0 2px 4px rgba(0,0,0,0.18);
    overflow: hidden;
  }
  .card-front { top: 130px; background: var(--card-white); }
  .card-back { top: 505px; background: var(--brand-blue); }

  .brand-mark {
    position: absolute; display: flex; align-items: center; gap: 10px;
    font-weight: 700; letter-spacing: 0.5px; line-height: 1;
  }
  .brand-dot { width: 14px; height: 14px; border-radius: 50%; }
  .card-front .brand-mark { right: 31px; top: 82px; font-size: 30px; color: var(--brand-blue); }
  .card-front .brand-dot { background: var(--ink-dark); }
  .card-back .brand-mark {
    left: 50%; top: 174px; transform: translateX(-50%);
    font-size: 38px; color: var(--card-white); white-space: nowrap;
  }
  .card-back .brand-dot { background: var(--ink-dark); width: 18px; height: 18px; }

  .holder-name {
    position: absolute; left: 32px; top: 213px;
    font-size: 22px; font-weight: 600; color: var(--brand-blue);
  }
  .name-rule {
    position: absolute; left: 32px; width: 552px; top: 242px;
    border-top: 1px solid var(--rule-grey);
  }
  .contact-list {
    position: absolute; left: 32px; top: 251px; list-style: none;
    font-size: 16px; color: var(--ink-text); line-height: 23px;
  }
  .contact-list li { display: flex; align-items: center; gap: 8px; }
  .contact-list svg { width: 14px; height: 14px; fill: var(--brand-blue); flex: none; }
  .address {
    position: absolute; right: 31px; top: 251px; text-align: right;
    font-style: normal; font-size: 16px; color: var(--ink-text); line-height: 23px;
  }
  .front-band { position: absolute; left: 0; bottom: 0; width: 615px; height: 40px; }
  .front-url {
    position: absolute; right: 27px; bottom: 7px;
    font-size: 17px; font-style: italic; color: var(--card-white); letter-spacing: 1.5px;
  }
  .back-url {
    position: absolute; left: 0; right: 0; top: 292px; text-align: center;
    font-size: 16px; color: var(--card-white); letter-spacing: 3.5px;
  }
</style>
</head>
<body>
<main class="canvas">
  <section class="card card-front" aria-label="Card front">
    <div class="brand-mark"><span class="brand-dot"></span>ROAM QUILL</div>
    <h1 class="holder-name">Bertrand Olesky</h1>
    <div class="name-rule"></div>
    <ul class="contact-list">
      <li>
        <svg viewBox="0 0 24 24" aria-hidden="true"><path d="M6.6 10.8a15.1 15.1 0 0 0 6.6 6.6l2.2-2.2c.3-.3.7-.4 1-.2 1.1.4 2.3.6 3.6.6.6 0 1 .4 1 1V20c0 .6-.4 1-1 1A17 17 0 0 1 3 4c0-.6.4-1 1-1h3.5c.6 0 1 .4 1 1 0 1.3.2 2.5.6 3.6.1.3 0 .7-.2 1z"/></svg>
        +1-(345)-402-7731
      </li>
      <li>
        <svg viewBox="0 0 24 24" aria-hidden="true"><path d="M2 5h20v14H2z M3.5 6.5 12 13l8.5-6.5" fill="none" stroke="#1ba5cf" stroke-width="2"/></svg>
        ceo@roamquill.net
      </li>
    </ul>
    <address class="address">Coral Reach Shore<br>Grand Cayman, Cayman Islands</address>
    <svg class="front-band" viewBox="0 0 615 40" aria-hidden="true">
      <path d="M0 12 H362 C352 21 346 23 332 23 H0 Z" fill="#222426"/>
      <path d="M340 40 C358 40 362 5 384 5 H615 V40 Z" fill="#1ba5cf"/>
    </svg>
    <span class="front-url">www.roamquill.net</span>
  </section>

  <section class="card card-back" aria-label="Card back">
    <div class="brand-mark"><span class="brand-dot"></span>ROAM QUILL</div>
    <span class="back-url">www.roamquill.net</span>
  </section>
</main>
</body>
</html>
```